OPF - Brochure 52 week Curriculum

Oak Path Fellows, Inc. wants to create a distribution Brochure. In the Bible (Matthew 28:18-20)- JESUS said to "TEACH" others what HE has commanded. we want to "PUT IN PRINT"

these 52 lines summarize HIS teachings
we want to use as our Curriculum teaching men ...

incorporate our statements and two main passages of scripture
(see attach pictures of headquarter lobby) to brand uniformity and consistency... we have summarized into 52 groups, but its NOT required to have numbers...
Purpose = obey GOD
Mission = love others
Vision = Development God fearing men globally.

The designer can have freedom in layout and sizing.
we were thinking bi fold , but again... designer has freedom
Please incorporate our colors (white, black, gray) using color wheel provided and our LOGO with website.

```html
<!DOCTYPE html>
<html lang="en">
<head>
<meta charset="utf-8">
<title>Oak Path Fellows – Curriculum Brochure Spread</title>
<link href="https://fonts.googleapis.com/css2?family=Poppins:ital,wght@0,300;0,400;0,600;0,800;0,900;1,300&display=swap" rel="stylesheet">
<style>
  :root {
    --backdrop: #b3d2d4;
    --paper: #ecebea;
    --paper-edge: #dcdbd9;
    --ink: #1b1b1b;
    --ink-soft: #3a3a3a;
    --accent-shadow: #5f8f93;
    --photo-light: #bdbdbd;
    --photo-mid: #7a7a7a;
    --photo-dark: #2c2c2c;
    --panel: rgba(40, 40, 40, 0.86);
    --panel-text: #f2f2f2;
    --panel-muted: #cfcfcf;
  }
  * { box-sizing: border-box; margin: 0; padding: 0; }
  html, body { width: 1200px; height: 700px; overflow: hidden; }
  body {
    background: var(--backdrop);
    font-family: "Poppins", sans-serif;
    color: var(--ink);
    position: relative;
  }
  .spread {
    position: absolute;
    left: 40px; top: 40px;
    width: 1120px; height: 620px;
    display: flex;
    box-shadow: 0 18px 40px rgba(0,0,0,0.18);
  }
  .page {
    position: relative;
    width: 560px; height: 620px;
    overflow: hidden;
  }
  /* Left page */
  .page--text {
    background: linear-gradient(90deg, var(--paper) 0%, var(--paper) 88%, var(--paper-edge) 100%);
    padding: 44px 44px 0 44px;
  }
  .section { margin-bottom: 22px; }
  .section__title {
    font-weight: 900;
    font-size: 23px;
    line-height: 1.05;
    text-transform: uppercase;
    letter-spacing: 0.3px;
    color: var(--ink);
    text-shadow: 2px 2px 0 var(--accent-shadow);
    margin-bottom: 10px;
  }
  .section__list { list-style: none; }
  .section__item {
    display: flex;
    align-items: flex-start;
    gap: 12px;
    font-size: 11.5px;
    font-weight: 300;
    line-height: 1.5;
    color: var(--ink-soft);
    margin-bottom: 5px;
  }
  .section__item--plain { padding-left: 26px; }
  .bullet { flex: 0 0 14px; margin-top: 4px; }
  .page__footer {
    position: absolute;
    font-size: 11px;
    line-height: 1;
    color: var(--ink-soft);
    white-space: nowrap;
  }
  .page--text .page__footer { right: 44px; bottom: 44px; }
  .page__footer strong { font-weight: 600; margin-right: 10px; }
  .page__footer .sep { margin-right: 10px; }
  .brand-name {
    position: absolute;
    font-weight: 900;
    font-size: 24px;
    line-height: 1;
    color: var(--ink);
    letter-spacing: 1px;
  }
  .page--text .brand-name { left: 44px; bottom: 38px; }

  /* Right page */
  .page--photo { background: var(--photo-light); }
  .photo {
    position: absolute; inset: 0;
    background:
      radial-gradient(ellipse at 75% 40%, var(--photo-mid) 0%, transparent 55%),
      linear-gradient(160deg, var(--photo-dark) 0%, var(--photo-mid) 45%, var(--photo-light) 80%);
  }
  .info-panel {
    position: absolute;
    left: 0; top: 0;
    width: 330px;
    padding: 36px 28px 26px 32px;
    background: var(--panel);
  }
  .info-panel__title {
    font-weight: 900;
    font-size: 21px;
    line-height: 1.05;
    text-transform: uppercase;
    color: var(--panel-text);
    text-shadow: 2px 2px 0 var(--accent-shadow);
    margin-bottom: 14px;
  }
  .info-panel .section__item { color: var(--panel-muted); font-size: 10.5px; }
  .page--photo .page__footer {
    bottom: 82px; right: 36px;
    color: var(--panel-text);
  }
  .page--photo .brand-name { left: 36px; bottom: 38px; }
</style>
</head>
<body>
<main class="spread">
  <section class="page page--text">
    <article class="section">
      <h2 class="section__title">Forgiveness (Jesus taught about the importance of both receiving and giving forgiveness)</h2>
      <ul class="section__list">
        <li class="section__item section__item--plain">Forgive others: Matthew 6:12, 14, Mark 11:25-26, Luke 6:37</li>
        <li class="section__item"><svg class="bullet" viewBox="0 0 14 10" width="14" height="10"><path d="M0 0 L7 5 L0 10 Z M6 0 L13 5 L6 10 L8 5 Z" fill="#1b1b1b"/></svg>JESUS emphasized that forgiveness is linked to forgiving others (Matthew 6:14-15)</li>
        <li class="section__item"><svg class="bullet" viewBox="0 0 14 10" width="14" height="10"><path d="M0 0 L7 5 L0 10 Z M6 0 L13 5 L6 10 L8 5 Z" fill="#1b1b1b"/></svg>forgiveness should be extended limitlessly to those who repent (Luke 17:3-4; Matthew 18:21-22).</li>
        <li class="section__item"><svg class="bullet" viewBox="0 0 14 10" width="14" height="10"><path d="M0 0 L7 5 L0 10 Z M6 0 L13 5 L6 10 L8 5 Z" fill="#1b1b1b"/></svg>forgiveness is also illustrated as the cancellation of debt (Matthew 18:21-35).</li>
      </ul>
    </article>
    <article class="section">
      <h2 class="section__title">Humility and Service</h2>
      <ul class="section__list">
        <li class="section__item"><svg class="bullet" viewBox="0 0 14 10" width="14" height="10"><path d="M0 0 L7 5 L0 10 Z M6 0 L13 5 L6 10 L8 5 Z" fill="#1b1b1b"/></svg>JESUS stated that humility leads to being honored (Luke 14:11; Matthew 23:12)</li>
        <li class="section__item"><svg class="bullet" viewBox="0 0 14 10" width="14" height="10"><path d="M0 0 L7 5 L0 10 Z M6 0 L13 5 L6 10 L8 5 Z" fill="#1b1b1b"/></svg>true greatness is found in serving others (Matthew 20:26-28).</li>
        <li class="section__item"><svg class="bullet" viewBox="0 0 14 10" width="14" height="10"><path d="M0 0 L7 5 L0 10 Z M6 0 L13 5 L6 10 L8 5 Z" fill="#1b1b1b"/></svg>The Bible also states that God opposes the proud but shows favor to the humble (James 4:6; 1 Peter 5:5).</li>
      </ul>
    </article>
    <article class="section">
      <h2 class="section__title">Warning against self-righteousness and judgment</h2>
      <ul class="section__list">
        <li class="section__item"><svg class="bullet" viewBox="0 0 14 10" width="14" height="10"><path d="M0 0 L7 5 L0 10 Z M6 0 L13 5 L6 10 L8 5 Z" fill="#1b1b1b"/></svg>Jesus warned against hypocrisy, particularly the hypocrisy of the Pharisees (Luke 12:1).</li>
      </ul>
    </article>
    <footer class="page__footer"><strong>Page 12</strong><span class="sep">|</span>oakpathfellows.org</footer>
    <div class="brand-name">OPF</div>
  </section>

  <section class="page page--photo">
    <div class="photo" role="img" aria-label="Black and white photograph of a man seated with hands clasped in prayer"></div>
    <div class="info-panel">
      <h2 class="info-panel__title">Money (Jesus taught about using money and possessions responsibly)</h2>
      <ul class="section__list">
        <li class="section__item"><svg class="bullet" viewBox="0 0 14 10" width="14" height="10"><path d="M0 0 L7 5 L0 10 Z M6 0 L13 5 L6 10 L8 5 Z" fill="#f2f2f2"/></svg>JESUS advised storing up treasures in Heaven rather than on Earth (Matthew 6:19-21)</li>
        <li class="section__item"><svg class="bullet" viewBox="0 0 14 10" width="14" height="10"><path d="M0 0 L7 5 L0 10 Z M6 0 L13 5 L6 10 L8 5 Z" fill="#f2f2f2"/></svg>JESUS stated that it is impossible to serve both God and money (Matthew 6:24).</li>
      </ul>
    </div>
    <footer class="page__footer"><strong>Page 13</strong><span class="sep">|</span>oakpathfellows.org</footer>
    <div class="brand-name">OPF</div>
  </section>
</main>
</body>
</html>
```